Brand new letterhead, business card, email signature etc.

We are a financial company in London, UK. Our website is www.quorvane.com. We're wanting a complete remodel of the company colours, letter head, business cards, email signatures, etc. Looking to keep the same font for the company name. I have upload a colour palette that we want to work with. We're looking for company letterhead for outgoing letters/ correspondence, letterhead for internal documentation, email signatures, e-letters. etc. Ultimately we will redesign the entire website also. It is important that our clients get a strong, secure, warm, trustworthy, solid feeling and first impression.
Updates

Designs look the same

Target Market(s)

Institutional investors, (ultra) high net worth individuals

Industry/Entity Type

Finance, Invesments banking.

Font styles to use
Other font styles liked:
• Current font is "Champagne & Limousines"

Requirements
Must have
• Must use the colours provided on the PDF uploaded to the portal. The purple = main colour. The red = accent colour.
Nice to have
• Nice to use same font as now for the company name "Marlowin". Font is "Champagne & Limousines". Nice to have some reference to the old logo flower, but only subtle.
Should not have
• Do not use the colour red from our website. Use the colours provided on the colour palette PDF that I uploaded in the portal.

```html
<!DOCTYPE html>
<html lang="en">
<head>
<meta charset="utf-8">
<title>Marlowin Business Card</title>
<link href="https://fonts.googleapis.com/css2?family=Josefin+Sans:wght@300;400;700&display=swap" rel="stylesheet">
<style>
  :root {
    --plum: #2b1219;
    --accent: #c2262e;
    --card: #ffffff;
    --backdrop: #e9e8ea;
    --shadow: rgba(20, 10, 15, 0.18);
  }
  * { box-sizing: border-box; margin: 0; padding: 0; }
  html, body {
    width: 1200px; height: 689px; overflow: hidden;
    background: var(--backdrop);
    font-family: "Josefin Sans", sans-serif;
    color: var(--plum);
  }
  .stage {
    width: 1200px; height: 689px;
    display: flex; align-items: center; justify-content: center; gap: 40px;
  }
  .card {
    width: 540px; height: 309px;
    background: var(--card);
    border-radius: 18px;
    box-shadow: 0 10px 30px var(--shadow);
    position: relative;
    overflow: hidden;
  }
  .brand { display: flex; align-items: center; }
  .brand-mark {
    border: 1.5px solid var(--plum);
    flex: none;
  }
  .brand-name {
    font-weight: 300;
    text-transform: uppercase;
    color: var(--plum);
    line-height: 1;
    white-space: nowrap;
  }

  /* Front */
  .card-front .brand {
    position: absolute; left: 42px; top: 50%; transform: translateY(-50%);
    gap: 22px;
  }
  .card-front .brand-mark { width: 86px; height: 86px; }
  .card-front .brand-name { font-size: 44px; letter-spacing: 0.18em; }

  /* Back */
  .card-back .brand {
    position: absolute; left: 30px; top: 196px; gap: 12px;
  }
  .card-back .brand-mark { width: 52px; height: 52px; }
  .card-back .brand-name { font-size: 26px; letter-spacing: 0.19em; }
  .divider {
    position: absolute; left: 318px; top: 62px; width: 1.5px; height: 160px;
    background: var(--plum);
  }
  .details {
    position: absolute; left: 334px; top: 64px; width: 192px;
  }
  .person-name {
    font-weight: 700; font-size: 16px; text-transform: uppercase; letter-spacing: -0.01em;
    white-space: nowrap;
  }
  .person-role { font-weight: 300; font-size: 11px; margin-top: 3px; }
  .contact-list { list-style: none; margin-top: 16px; }
  .contact-list li {
    display: flex; align-items: center; gap: 7px;
    font-weight: 300; font-size: 11px; line-height: 1.75;
    white-space: nowrap;
  }
  .contact-list svg { width: 10px; height: 10px; flex: none; fill: var(--plum); }
  .address { font-style: normal; font-weight: 300; font-size: 11px; line-height: 1.5; margin-top: 14px; white-space: nowrap; }
</style>
</head>
<body>
<main class="stage">
  <section class="card card-front" aria-label="Business card front">
    <div class="brand">
      <span class="brand-mark"></span>
      <span class="brand-name">Marlowin</span>
    </div>
  </section>

  <section class="card card-back" aria-label="Business card back">
    <div class="brand">
      <span class="brand-mark"></span>
      <span class="brand-name">Marlowin</span>
    </div>
    <span class="divider"></span>
    <div class="details">
      <p class="person-name">Adrian Holloway</p>
      <p class="person-role">Managing Director</p>
      <ul class="contact-list">
        <li>
          <svg viewBox="0 0 10 10" aria-hidden="true"><path d="M2 0.5 L3.6 2.6 L2.7 3.6 Q3.8 5.9 6.2 7.2 L7.2 6.3 L9.5 7.8 L8.4 9.5 Q4.5 9.3 1.9 6.2 Q0.2 3.9 0.6 1.5 Z"/></svg>
          020 7946 0321
        </li>
        <li>
          <svg viewBox="0 0 10 10" aria-hidden="true"><path d="M0.5 2 H9.5 V8.5 H0.5 Z M1 2.5 L5 5.6 L9 2.5" fill="none" stroke="#2b1219" stroke-width="1"/><path d="M0.5 2 H9.5 L5 5.4 Z"/></svg>
          info@quorvane.com
        </li>
        <li>
          <svg viewBox="0 0 10 10" aria-hidden="true"><circle cx="5" cy="5" r="4.3" fill="none" stroke="#2b1219" stroke-width="1"/><ellipse cx="5" cy="5" rx="1.8" ry="4.3" fill="none" stroke="#2b1219" stroke-width="0.8"/><path d="M0.8 5 H9.2" stroke="#2b1219" stroke-width="0.8"/></svg>
          www.quorvane.com
        </li>
      </ul>
      <address class="address">
        Marlowin Group Limited 11th Floor<br>
        18 Ferrier Lane London EC3V 9QT
      </address>
    </div>
  </section>
</main>
</body>
</html>
```